App Design

This is a 'video player' app - will be used to stream video files and watch them on a device. Need 3/4 skins for user customization.
Design will need to be versatile - used on: Kestrel4/4S/5 and vexTab2/3
Require an app design that shows the required functionality described by us, allows ease to navigate and visually creates a unique user experience.
App must have following pages: (refer to attached pages)
1. Search Page
2. Results Page
3. Video Page
4. End Page
3-4 skins for user preference
important: if you are interested please submit designs by tomorrow night - we will be picking from submitted designs - will make revisions and finalize the design within 4-5 days.
timing is crucial- please only submit if you can commit to timeline and design requirements. There will be refinements required.
Please see the attached update.
Additional reference files have been added to help in your efforts.
We have added a sample design that may help with your submissions. Please see brief
Target Market(s)
early adapters for technology / kestrel, tablet, zorbix users
Requirements
Should not have
- should not be generic design

```html
<!DOCTYPE html>
<html lang="en">
<head>
<meta charset="utf-8">
<title>Reelwave – Video Player App Screens</title>
<link rel="stylesheet" href="https://fonts.googleapis.com/css2?family=Arimo:wght@400;700&family=Open+Sans:wght@400;600&family=Raleway:wght@300&display=swap">
<style>
:root{
  --stage:#9b6aa9;
  --purple:#9a5fb0;
  --purple-dark:#7c4393;
  --purple-deep:#6a3380;
  --peach-top:#fde3c8;
  --peach-mid:#f9b98a;
  --coral:#f07a5c;
  --red:#d9384a;
  --orange:#f66a36;
  --cell:#f4f1f2;
  --ink:#2b2b2b;
  --muted:#555;
  --white:#fff;
}
*{box-sizing:border-box;margin:0;padding:0}
html,body{width:1200px;height:795px;overflow:hidden}
body{background:var(--stage);font-family:"Open Sans",Arial,sans-serif;position:relative}
.screen{position:absolute;top:157px;width:320px;height:480px;overflow:hidden;
  background:linear-gradient(180deg,var(--peach-top) 0%,var(--peach-mid) 45%,var(--coral) 80%,var(--red) 100%);
  box-shadow:0 10px 30px rgba(60,20,80,.35)}
.screen--splash{left:60px;background:linear-gradient(170deg,#fff1e4 0%,#fbd2ad 35%,#f5a57d 65%,#e0545a 88%,#c93a4f 100%)}
.screen--results{left:440px}
.screen--video{left:820px}
.status-bar{position:absolute;top:0;left:0;width:320px;height:20px;
  background:linear-gradient(180deg,#f4f6f8,#c9ced4);display:flex;align-items:center;
  font-family:Arimo,Arial,sans-serif;font-size:12px;color:#222;padding:0 5px}
.status-bar .carrier{margin-left:3px;font-weight:700;font-size:11px}
.status-bar .time{position:absolute;left:0;right:0;text-align:center;font-weight:700;font-size:13px}
.status-bar .battery{margin-left:auto}
.nav-bar{position:absolute;top:20px;left:0;width:320px;height:44px;
  background:linear-gradient(180deg,#b07bc4,var(--purple) 50%,var(--purple-dark));
  border-bottom:1px solid var(--purple-deep)}
.nav-bar .back{position:absolute;left:8px;top:8px;width:56px;height:29px}
.nav-bar .title{position:absolute;left:0;right:0;top:10px;text-align:center;
  font-family:Arimo,Arial,sans-serif;font-weight:700;font-size:20px;color:var(--white);
  text-shadow:0 -1px 0 rgba(0,0,0,.3)}
.search{position:absolute;top:70px;left:12px;width:296px;height:38px;background:var(--white);
  border-radius:6px;box-shadow:inset 0 1px 3px rgba(0,0,0,.25)}
.search .icon{position:absolute;left:8px;top:6px}
.search .placeholder{position:absolute;left:46px;top:8px;font-family:Arimo,Arial,sans-serif;font-size:19px;color:#b5b5b5}
.search .clear{position:absolute;right:8px;top:7px}
.result{position:absolute;left:9px;width:303px;height:65px;background:var(--cell);display:flex}
.result .thumb{width:103px;height:65px}
.result .info{padding:8px 0 0 28px;flex:1;position:relative}
.result h3{font-size:12.5px;font-weight:600;color:var(--ink);white-space:nowrap}
.result p{font-size:9.5px;line-height:11px;color:var(--muted);margin-top:5px;width:140px}
.result .chev{position:absolute;right:10px;top:27px}
.thumb--stripes{background:linear-gradient(90deg,#c9677a,#e0a0a2 40%,#b94a62 70%,#dca9a4)}
.thumb--dots{background:linear-gradient(135deg,#f27f86,#f6a38a)}
.thumb--glow{background:radial-gradient(ellipse at 40% 60%,#f7c8c3,#d2476d 70%)}
.thumb--light{background:linear-gradient(120deg,#d7a399,#f0d3bd 50%,#f7efc8)}
.tab-bar{position:absolute;bottom:0;left:0;width:320px;height:48px;display:flex;
  background:linear-gradient(180deg,#b27cc6,var(--purple-dark));border-top:1px solid #c79bd6}
.tab{flex:1;text-align:center;color:var(--white);font-family:Arimo,Arial,sans-serif;font-weight:700;font-size:12px;padding-top:4px;border-right:1px solid rgba(0,0,0,.12)}
.tab svg{display:block;margin:0 auto 1px}
.tab--active{background:linear-gradient(180deg,#ff8a55,var(--orange))}
.splash-name{position:absolute;top:126px;left:0;right:0;text-align:center;
  font-family:"Open Sans",Arial,sans-serif;font-weight:600;font-size:26px;color:var(--purple-dark)}
.splash-mark{position:absolute;left:122px;top:180px;width:76px;height:76px;background:var(--purple);border-radius:4px}
.legal{position:absolute;left:15px;bottom:18px;width:300px;font-family:Raleway,Arial,sans-serif;
  font-size:10px;line-height:13px;color:var(--white);letter-spacing:.1px}
.player{position:absolute;top:128px;left:8px;width:304px;height:184px;border:4px solid #f2eeee;
  background:radial-gradient(ellipse at 85% 90%,#f7f0c4 0%,transparent 45%),linear-gradient(135deg,#8e3553,#c76d7d 45%,#e9b6a5 80%,#f0cfb7)}
.player .play{position:absolute;left:108px;top:48px}
.caption{position:absolute;top:312px;left:8px;width:304px;height:100px;background:rgba(245,242,243,.95);padding:22px 14px 0}
.caption h3{font-size:12.5px;font-weight:600;color:var(--ink)}
.caption p{font-size:10px;line-height:11.5px;color:var(--muted);margin-top:9px}
</style>
</head>
<body>

<section class="screen screen--splash" aria-label="Splash screen">
  <div class="status-bar">
    <svg width="20" height="10"><rect x="0" y="7" width="3" height="3" fill="#2a5db0"/><rect x="4" y="5" width="3" height="5" fill="#2a5db0"/><rect x="8" y="3" width="3" height="7" fill="#2a5db0"/><rect x="12" y="1" width="3" height="9" fill="#2a5db0"/><rect x="16" y="0" width="3" height="10" fill="#2a5db0"/></svg>
    <span class="carrier">MERLO</span>
    <svg style="margin-left:14px" width="16" height="11" viewBox="0 0 16 11"><path d="M1 4a10 10 0 0 1 14 0M3.5 6.5a6.5 6.5 0 0 1 9 0M6 9a3 3 0 0 1 4 0" stroke="#2a5db0" stroke-width="1.7" fill="none"/></svg>
    <span class="time">1:09 PM</span>
    <svg class="battery" width="22" height="10"><rect x=".5" y=".5" width="18" height="9" fill="#fff" stroke="#555"/><rect x="2" y="2" width="15" height="6" fill="#3cb83c"/><rect x="19" y="3" width="2" height="4" fill="#555"/></svg>
  </div>
  <h1 class="splash-name">Reelwave</h1>
  <div class="splash-mark" aria-hidden="true"></div>
  <p class="legal">TECHNOLOGY IS PROJECTED BY XX PENDING PATENTS AND YY PENDING TRADEMARKS. DO NOT INFRINGE.</p>
</section>

<section class="screen screen--results" aria-label="Search results screen">
  <div class="status-bar">
    <svg width="20" height="10"><rect x="0" y="7" width="3" height="3" fill="#2a5db0"/><rect x="4" y="5" width="3" height="5" fill="#2a5db0"/><rect x="8" y="3" width="3" height="7" fill="#2a5db0"/><rect x="12" y="1" width="3" height="9" fill="#2a5db0"/><rect x="16" y="0" width="3" height="10" fill="#2a5db0"/></svg>
    <span class="carrier">MERLO</span>
    <svg style="margin-left:14px" width="16" height="11" viewBox="0 0 16 11"><path d="M1 4a10 10 0 0 1 14 0M3.5 6.5a6.5 6.5 0 0 1 9 0M6 9a3 3 0 0 1 4 0" stroke="#2a5db0" stroke-width="1.7" fill="none"/></svg>
    <span class="time">1:09 PM</span>
    <svg class="battery" width="22" height="10"><rect x=".5" y=".5" width="18" height="9" fill="#fff" stroke="#555"/><rect x="2" y="2" width="15" height="6" fill="#3cb83c"/><rect x="19" y="3" width="2" height="4" fill="#555"/></svg>
  </div>
  <header class="nav-bar">
    <svg class="back" viewBox="0 0 56 29"><path d="M12 1H52a3 3 0 0 1 3 3V25a3 3 0 0 1-3 3H12L1 14.5Z" fill="#6e3785" stroke="#5a2a6e"/><text x="32" y="19" text-anchor="middle" font-family="Arimo,Arial,sans-serif" font-weight="700" font-size="12" fill="#fff">Back</text></svg>
    <div class="title">Reelwave</div>
  </header>
  <div class="search">
    <svg class="icon" width="28" height="26" viewBox="0 0 28 26"><circle cx="11" cy="10" r="7.5" stroke="#8e56a8" stroke-width="3" fill="#fff"/><path d="M16.5 16 24 23" stroke="#6a3380" stroke-width="4.5" stroke-linecap="round"/></svg>
    <span class="placeholder">Search</span>
    <svg class="clear" width="24" height="24"><circle cx="12" cy="12" r="11" fill="#8e56a8"/><path d="M8 8l8 8M16 8l-8 8" stroke="#fff" stroke-width="2.6" stroke-linecap="round"/></svg>
  </div>
  <article class="result" style="top:113px">
    <div class="thumb thumb--stripes" role="img" aria-label="Show thumbnail photo"></div>
    <div class="info"><h3>Weekend Late Show</h3><p>Lorem ipsum dolor sit amet, consectetur adipiscing elit</p>
      <svg class="chev" width="7" height="10"><path d="M1 1l4 4-4 4" stroke="#333" stroke-width="1.8" fill="none"/></svg></div>
  </article>
  <article class="result" style="top:195px">
    <div class="thumb thumb--dots" role="img" aria-label="Show thumbnail photo"></div>
    <div class="info"><h3>Late night with Jona…</h3><p>Phasellus dictum ante eget urna feugiat non figuranti …</p>
      <svg class="chev" width="7" height="10"><path d="M1 1l4 4-4 4" stroke="#333" stroke-width="1.8" fill="none"/></svg></div>
  </article>
  <article class="result" style="top:277px">
    <div class="thumb thumb--glow" role="img" aria-label="Show thumbnail photo"></div>
    <div class="info"><h3>Nation's Star Stage</h3><p>Lorem ipsum dolor sit amet, consectetur adipiscing elit.</p>
      <svg class="chev" width="7" height="10"><path d="M1 1l4 4-4 4" stroke="#333" stroke-width="1.8" fill="none"/></svg></div>
  </article>
  <article class="result" style="top:360px">
    <div class="thumb thumb--light" role="img" aria-label="Show thumbnail photo"></div>
    <div class="info"><h3>Late night with Jona…</h3><p>Lorem ipsum dolor sit amet, consectetur adipiscing elit…</p>
      <svg class="chev" width="7" height="10"><path d="M1 1l4 4-4 4" stroke="#333" stroke-width="1.8" fill="none"/></svg></div>
  </article>
  <nav class="tab-bar">
    <div class="tab"><svg width="26" height="24" viewBox="0 0 26 24"><path d="M12 22 3 13a5.5 5.5 0 0 1 9-7 5.5 5.5 0 0 1 9 7Z" fill="#fff"/><circle cx="20" cy="17" r="5" fill="#fff" stroke="#8e56a8" stroke-width="1.5"/><path d="M20 14v6M17 17h6" stroke="#8e56a8" stroke-width="1.6"/></svg>name</div>
    <div class="tab"><svg width="30" height="24" viewBox="0 0 30 24"><circle cx="11" cy="7" r="5" fill="#fff"/><path d="M2 22c0-6 4-9 9-9s9 3 9 9Z" fill="#fff"/><circle cx="20" cy="7" r="4.5" fill="#fff"/><path d="M17 13c6 0 11 3 11 9h-7" fill="#fff"/></svg>name</div>
    <div class="tab tab--active"><svg width="26" height="24" viewBox="0 0 26 24"><circle cx="10" cy="9" r="7" stroke="#fff" stroke-width="3" fill="none"/><path d="M15 14l7 7" stroke="#fff" stroke-width="4" stroke-linecap="round"/></svg>name</div>
    <div class="tab"><svg width="26" height="24" viewBox="0 0 26 24"><path d="M4 21 19 6M20 3l3 3-3 3-3-3Z" stroke="#fff" stroke-width="3" fill="#fff"/><path d="M6 4l14 14" stroke="#fff" stroke-width="3.5"/><circle cx="6" cy="4" r="3.5" fill="#fff"/></svg>name</div>
  </nav>
</section>

<section class="screen screen--video" aria-label="Video screen">
  <div class="status-bar">
    <svg width="20" height="10"><rect x="0" y="7" width="3" height="3" fill="#2a5db0"/><rect x="4" y="5" width="3" height="5" fill="#2a5db0"/><rect x="8" y="3" width="3" height="7" fill="#2a5db0"/><rect x="12" y="1" width="3" height="9" fill="#2a5db0"/><rect x="16" y="0" width="3" height="10" fill="#2a5db0"/></svg>
    <span class="carrier">MERLO</span>
    <svg style="margin-left:14px" width="16" height="11" viewBox="0 0 16 11"><path d="M1 4a10 10 0 0 1 14 0M3.5 6.5a6.5 6.5 0 0 1 9 0M6 9a3 3 0 0 1 4 0" stroke="#2a5db0" stroke-width="1.7" fill="none"/></svg>
    <span class="time">1:09 PM</span>
    <svg class="battery" width="22" height="10"><rect x=".5" y=".5" width="18" height="9" fill="#fff" stroke="#555"/><rect x="2" y="2" width="15" height="6" fill="#3cb83c"/><rect x="19" y="3" width="2" height="4" fill="#555"/></svg>
  </div>
  <header class="nav-bar">
    <svg class="back" viewBox="0 0 56 29"><path d="M12 1H52a3 3 0 0 1 3 3V25a3 3 0 0 1-3 3H12L1 14.5Z" fill="#6e3785" stroke="#5a2a6e"/><text x="32" y="19" text-anchor="middle" font-family="Arimo,Arial,sans-serif" font-weight="700" font-size="12" fill="#fff">Back</text></svg>
    <div class="title">Reelwave</div>
  </header>
  <div class="search">
    <svg class="icon" width="28" height="26" viewBox="0 0 28 26"><circle cx="11" cy="10" r="7.5" stroke="#8e56a8" stroke-width="3" fill="#fff"/><path d="M16.5 16 24 23" stroke="#6a3380" stroke-width="4.5" stroke-linecap="round"/></svg>
    <span class="placeholder">Search</span>
    <svg class="clear" width="24" height="24"><circle cx="12" cy="12" r="11" fill="#8e56a8"/><path d="M8 8l8 8M16 8l-8 8" stroke="#fff" stroke-width="2.6" stroke-linecap="round"/></svg>
  </div>
  <div class="player" role="img" aria-label="Video frame still from the show">
    <svg class="play" width="80" height="80"><circle cx="40" cy="40" r="39" fill="rgba(255,255,255,.25)"/><path d="M34 28v24l18-12Z" fill="#fff"/></svg>
  </div>
  <div class="caption">
    <h3>Late night with Jonah at the show.</h3>
    <p>Lorem ipsum dolor sit amet, Lorem ipsum dolor sit amet, consectetur adipiscing elit.Lorem ipsum dolor sit amet, consectetur adipiscing elit.</p>
  </div>
  <nav class="tab-bar">
    <div class="tab"><svg width="26" height="24" viewBox="0 0 26 24"><path d="M12 22 3 13a5.5 5.5 0 0 1 9-7 5.5 5.5 0 0 1 9 7Z" fill="#fff"/><circle cx="20" cy="17" r="5" fill="#fff" stroke="#8e56a8" stroke-width="1.5"/><path d="M20 14v6M17 17h6" stroke="#8e56a8" stroke-width="1.6"/></svg>name</div>
    <div class="tab"><svg width="30" height="24" viewBox="0 0 30 24"><circle cx="11" cy="7" r="5" fill="#fff"/><path d="M2 22c0-6 4-9 9-9s9 3 9 9Z" fill="#fff"/><circle cx="20" cy="7" r="4.5" fill="#fff"/><path d="M17 13c6 0 11 3 11 9h-7" fill="#fff"/></svg>name</div>
    <div class="tab tab--active"><svg width="26" height="24" viewBox="0 0 26 24"><circle cx="10" cy="9" r="7" stroke="#fff" stroke-width="3" fill="none"/><path d="M15 14l7 7" stroke="#fff" stroke-width="4" stroke-linecap="round"/></svg>name</div>
    <div class="tab"><svg width="26" height="24" viewBox="0 0 26 24"><path d="M4 21 19 6M20 3l3 3-3 3-3-3Z" stroke="#fff" stroke-width="3" fill="#fff"/><path d="M6 4l14 14" stroke="#fff" stroke-width="3.5"/><circle cx="6" cy="4" r="3.5" fill="#fff"/></svg>name</div>
  </nav>
</section>

</body>
</html>
```